Website Design and Build

This is a design and build of a dating site.

100% the most important thing is for the website to look good. I want this thing to be stunning and feel like a premium product so please only tender for the job if you excel at design and use of colours.

Theme is: premium, professional & uncluttered
Colour Scheme is: bright, fun and friendly but also reassuring and professional
 
Platforms: Initially just browser based (desktop and mobile) but if the proof of concept works we will roll it out to apps across the major platforms.

Marketing will be done primarily through organic online searches and content driven leads to a squeeze page, so SEO optimisation and experience with squeeze pages also a must.

Please include examples of sites you’ve done or other sites you think give a flavour of your vision for what this site will be. Any thoughts on palettes/colour scheme also useful.

I will provide the full brief to the successful designer.

Thank you for your time.

Industry/Entity Type

Dating

Coding

Coded - Design and coding required

Number of Pages Required

5+ page

Font styles to use
Sans Serif

Colors

Designer to choose colors to be used in the design.

Requirements
Must have
• Professional, Premium and uncluttered look.
• SEO optimisation.
• Squeeze page.
• A way to track different lead sources e.g. some of it will be content led to a squeeze page, some of it organic search engine hits, some of it unique referral links given to specific bloggers/influencers. I want to be able to track the success of all the different types of generating traffic to the site.
• I also want to be able to amend/update the site myself going forward so would like the spec/design to be clearly documented to allow me to do this.

```html
<!DOCTYPE html>
<html lang="en">
<head>
<meta charset="utf-8">
<title>Amarelle – Dating</title>
<link href="https://fonts.googleapis.com/css2?family=Poppins:wght@400;500;600;700&family=Open+Sans:wght@400;600&display=swap" rel="stylesheet">
<style>
:root{
  --teal:#27b49a;
  --coral:#ef5659;
  --ink:#26252f;
  --night:#23222e;
  --grey-band:#ececee;
  --text:#6d6d76;
  --white:#ffffff;
  --line:#dcdce0;
}
*{box-sizing:border-box;margin:0;padding:0}
html,body{width:1200px;height:4627px;overflow:hidden;background:var(--white)}
body{font-family:"Open Sans",Arial,sans-serif;color:var(--text)}
.page{position:relative;width:1200px;height:4627px;overflow:hidden}
.abs{position:absolute}
.heading{font-family:"Poppins",Arial,sans-serif;font-weight:700;color:var(--ink);font-size:30px;letter-spacing:.5px;text-transform:uppercase;text-align:center;width:1200px;left:0}
.heading span,.accent{color:var(--teal)}
.body-text{font-size:13px;line-height:22px;color:var(--text)}
.btn{position:absolute;display:flex;align-items:center;justify-content:center;border-radius:22px;font-family:"Poppins",Arial,sans-serif;font-weight:600;font-size:13px;color:var(--white);text-transform:uppercase;letter-spacing:.5px}
.btn--coral{background:var(--coral)}
.btn--teal{background:var(--teal)}

/* header */
.hero{left:0;top:0;width:1200px;height:700px;background:linear-gradient(100deg,#e9d6bf 0%,#c9a684 22%,#9a7a63 38%,#c8b8a4 55%,#e2d6c6 75%,#b9b3aa 100%)}
.logo{left:163px;top:30px;font-family:"Poppins",Arial,sans-serif;font-weight:500;font-size:26px;color:var(--teal);display:flex;align-items:center;gap:8px}
.logo i{width:10px;height:10px;border-radius:50%;background:var(--teal);display:block}
.nav{left:361px;top:33px;display:flex;gap:34px;font-family:"Poppins",Arial,sans-serif;font-size:12px;font-weight:500;color:#3a3a44;text-transform:uppercase}
.nav .is-active,.nav .login{color:var(--teal)}
.register{left:954px;top:24px;width:84px;height:38px;font-size:12px}

/* signup */
.signup{left:706px;top:210px;width:332px;height:424px;background:var(--white);box-shadow:0 6px 24px rgba(0,0,0,.18);padding:28px 26px}
.signup h2{font-family:"Poppins",Arial,sans-serif;font-weight:700;font-size:22px;color:var(--ink);text-align:center;text-transform:uppercase;margin-bottom:26px}
.field{display:flex;align-items:center;height:30px;margin-bottom:13px;font-size:12px;color:var(--ink)}
.field label{width:82px}
.field .input{flex:1;height:30px;border:1px solid var(--line);border-radius:3px;font-size:11px;color:#a5a5ad;padding-left:8px;display:flex;align-items:center}
.gender{display:flex;gap:4px}
.gender b{width:26px;height:26px;border-radius:3px;display:block}
.gender .m{background:#d8d8dc}.gender .f{background:var(--coral)}
.start{left:100px;top:372px;width:208px;height:34px}

/* steps */
.step{top:966px;width:300px;text-align:center}
.step .ring{width:134px;height:134px;border-radius:50%;border:3px solid var(--teal);padding:5px;margin:0 auto}
.step .disc{width:100%;height:100%;border-radius:50%;background:var(--teal);display:flex;align-items:center;justify-content:center}
.step h3{font-family:"Poppins",Arial,sans-serif;font-weight:700;font-size:16px;color:var(--ink);text-transform:uppercase;margin:26px 0 10px}

/* members */
.member{width:172px;height:174px}
.member-tag{left:222px;top:1640px;font-size:12px;color:var(--white);font-weight:600}

/* story */
.story-photo{left:163px;top:2298px;width:411px;height:282px;background:linear-gradient(180deg,#b9a892 0%,#8d7a6a 55%,#6f6256 100%)}
.quote-mark{left:626px;top:2296px;font-family:"Poppins",Arial,sans-serif;font-weight:700;font-size:40px;color:var(--coral);line-height:1}
.story-text{left:626px;top:2300px;width:412px;font-size:12px;line-height:21px}
.story-name{left:626px;top:2494px;font-size:12px;color:var(--teal);font-weight:600}
.story-name small{color:var(--text);font-weight:400}
.arrow{width:30px;height:30px;border-radius:50%;background:#cfcfd4;display:flex;align-items:center;justify-content:center}

/* dark band */
.easy-text{left:330px;top:2860px;width:540px;text-align:center;color:#b6b5c0}
.easy-input{left:386px;top:2940px;width:284px;height:38px;background:var(--white);border-radius:20px;font-size:11px;color:#999;padding-left:16px;display:flex;align-items:center}

/* app */
.app-title{left:163px;top:3255px;font-family:"Poppins",Arial,sans-serif;font-weight:700;font-size:30px;color:var(--ink);text-transform:uppercase}
.app-text{left:163px;top:3320px;width:430px}

/* blog */
.card{top:3801px;width:266px;height:420px;background:var(--white);box-shadow:0 2px 10px rgba(0,0,0,.06)}
.card .pic{height:196px}
.card h4{font-family:"Poppins",Arial,sans-serif;font-weight:600;font-size:15px;line-height:22px;color:var(--ink);margin:20px 14px 10px}
.card .meta{margin:0 14px 12px;font-size:10px;color:var(--teal);display:flex;gap:16px}
.card p{margin:0 14px;font-size:11px;line-height:19px}

/* footer */
.support{left:163px;top:4425px;color:var(--white)}
.support .label{font-family:"Poppins",Arial,sans-serif;font-size:13px;font-weight:600}
.support .phone{font-family:"Poppins",Arial,sans-serif;font-size:27px;font-weight:700;color:var(--teal);line-height:36px}
.social{display:flex;gap:6px;margin-top:6px}
.social i{width:24px;height:24px;border-radius:50%;border:1.5px solid var(--white);display:block}
.footer-col{top:4392px}
.footer-col h5{font-family:"Poppins",Arial,sans-serif;font-weight:600;font-size:16px;color:var(--teal);margin-bottom:10px}
.footer-col li{list-style:none;font-size:11px;line-height:19px;color:#c9c8d2}
.copyright{left:0;top:4588px;width:1200px;text-align:center;font-size:11px;color:#c9c8d2}
.footer-rule{left:163px;top:4572px;width:874px;height:1px;background:#3b3a48}
</style>
</head>
<body>
<div class="page">

  <!-- background bands -->
  <svg class="abs" style="left:0;top:0" width="1200" height="4627" aria-hidden="true">
    <polygon points="0,1450 1200,1285 1200,2060 0,2140" fill="var(--grey-band)"/>
    <polygon points="0,2722 1200,2634 1200,3092 0,3180" fill="var(--night)"/>
    <polygon points="0,3600 1200,3560 1200,4300 0,4330" fill="var(--grey-band)"/>
    <polygon points="650,4302 1200,4258 1200,4272 650,4316" fill="var(--teal)"/>
    <polygon points="0,4330 1200,4272 1200,4627 0,4627" fill="var(--night)"/>
  </svg>

  <!-- hero -->
  <div class="abs hero" role="img" aria-label="Photo of a young couple embracing on a beach at sunset"></div>
  <svg class="abs" style="left:0;top:600px" width="1200" height="110" aria-hidden="true">
    <polygon points="0,100 1200,54 1200,110 0,110" fill="var(--white)"/>
    <polygon points="760,71 1200,40 1200,54 760,85" fill="var(--teal)"/>
  </svg>

  <div class="abs logo">Amarelle<i></i></div>
  <nav class="abs nav">
    <span class="is-active">Home</span><span>Members</span><span>Why choose us</span><span>About</span><span>Premium</span><span>Contact</span><span class="login">Login</span>
  </nav>
  <div class="btn btn--coral register">Register</div>

  <div class="abs signup">
    <h2>Sign up <span class="accent">for free!</span></h2>
    <div class="field"><label>I am</label><div class="gender"><b class="m"></b><b class="f"></b></div></div>
    <div class="field"><label>Age</label><div class="input">Select Your Age</div></div>
    <div class="field"><label>Email</label><div class="input"></div></div>
    <div class="field"><label>Password</label><div class="input"></div></div>
    <div class="field"><label>Postal code</label><div class="input">90210</div></div>
    <div class="btn btn--teal start">Start now</div>
  </div>

  <!-- how it works -->
  <h2 class="abs heading" style="top:850px">How does it <span>work?</span></h2>
  <div class="abs step" style="left:137px">
    <div class="ring"><div class="disc">
      <svg width="52" height="52" viewBox="0 0 52 52" aria-hidden="true"><circle cx="26" cy="17" r="10" fill="#fff"/><path d="M6 48c0-12 9-18 20-18s20 6 20 18z" fill="#fff"/></svg>
    </div></div>
    <h3>Create a profile</h3>
    <p class="body-text">Sed ut perspiciatis unde omnis iste natus error sit voluptatem accusantium doloremque laudantium, totam rem aperiam, eaque ipsa quae.</p>
  </div>
  <div class="abs step" style="left:450px">
    <div class="ring"><div class="disc">
      <svg width="52" height="52" viewBox="0 0 52 52" aria-hidden="true"><circle cx="22" cy="22" r="14" fill="none" stroke="#fff" stroke-width="5"/><line x1="32" y1="32" x2="46" y2="46" stroke="#fff" stroke-width="6" stroke-linecap="round"/></svg>
    </div></div>
    <h3>Find matches</h3>
    <p class="body-text">Sed ut perspiciatis unde omnis iste natus error sit voluptatem accusantium doloremque laudantium, totam rem aperiam, eaque ipsa quae.</p>
  </div>
  <div class="abs step" style="left:763px">
    <div class="ring"><div class="disc">
      <svg width="52" height="52" viewBox="0 0 52 52" aria-hidden="true"><path d="M26 46 8 28a10 10 0 0 1 18-12 10 10 0 0 1 18 12z" fill="#fff"/></svg>
    </div></div>
    <h3>Start dating</h3>
    <p class="body-text">Sed ut perspiciatis unde omnis iste natus error sit voluptatem accusantium doloremque laudantium, totam rem aperiam, eaque ipsa quae.</p>
  </div>

  <!-- recently joined -->
  <h2 class="abs heading" style="top:1480px">Recently joined <span>Amarelle</span></h2>
  <div class="abs member" style="left:163px;top:1558px;background:linear-gradient(160deg,#6a4b38,#b0875f)" role="img" aria-label="Member photo"></div>
  <div class="abs member" style="left:338px;top:1558px;background:linear-gradient(160deg,#2fae97,#1f8674)" role="img" aria-label="Member photo with teal overlay"></div>
  <div class="abs member" style="left:513px;top:1558px;background:linear-gradient(160deg,#d9b07a,#9c7a4c)" role="img" aria-label="Member photo"></div>
  <div class="abs member" style="left:688px;top:1558px;background:linear-gradient(160deg,#8d735f,#4f4a48)" role="img" aria-label="Member photo"></div>
  <div class="abs member" style="left:863px;top:1558px;background:linear-gradient(160deg,#9a8c7c,#5e5248)" role="img" aria-label="Member photo"></div>
  <div class="abs member" style="left:163px;top:1738px;background:linear-gradient(160deg,#3a3130,#7a5c44)" role="img" aria-label="Member photo"></div>
  <div class="abs member" style="left:338px;top:1738px;background:linear-gradient(160deg,#4d3a33,#a0714f)" role="img" aria-label="Member photo"></div>
  <div class="abs member" style="left:513px;top:1738px;background:linear-gradient(160deg,#c9a177,#6e5647)" role="img" aria-label="Member photo"></div>
  <div class="abs member" style="left:688px;top:1738px;background:linear-gradient(160deg,#c7b8a6,#7a6251)" role="img" aria-label="Member photo"></div>
  <div class="abs member" style="left:863px;top:1738px;background:linear-gradient(160deg,#d6d2cc,#9b9088)" role="img" aria-label="Member photo"></div>
  <svg class="abs" style="left:409px;top:1606px" width="30" height="28" viewBox="0 0 52 48" aria-hidden="true"><path d="M26 46 8 28a10 10 0 0 1 18-12 10 10 0 0 1 18 12z" fill="#fff"/></svg>
  <div class="abs member-tag" style="left:378px">Los Angeles, 28</div>
  <div class="btn btn--coral" style="left:487px;top:1965px;width:226px;height:42px">Meet someone special</div>

  <!-- stories -->
  <h2 class="abs heading" style="top:2206px">Dating success <span>stories</span></h2>
  <div class="abs story-photo" role="img" aria-label="Photo of a happy couple walking on a beach"></div>
  <div class="abs quote-mark">&ldquo;</div>
  <p class="abs story-text" style="top:2340px">Lorem ipsum dolor sit amet, consecte tur adipisc elit dolo. Proin ultricies vestibulum velit 3ab endum et condimentu mimetusp dolore ipsum doucibus sed dolorerem ipsu.Lorem ipsum dolor sit amet, consecte tur adipisc elit dolo. Proin ultricies vestibulum velit 3ab endum et condimentu mimetusp dolore ipsum doucibus sed dolorem ipproin ultricies vestibulum velit 3ab endum et condimentu mimetusp dolore doucibus sed dolorerem ipsu.</p>
  <div class="abs story-name">Dana, <small>26 years old</small></div>
  <div class="abs arrow" style="left:632px;top:2540px"><svg width="10" height="10" viewBox="0 0 10 10" aria-hidden="true"><path d="M7 1 3 5l4 4" stroke="#fff" stroke-width="2" fill="none"/></svg></div>
  <div class="abs arrow" style="left:692px;top:2540px"><svg width="10" height="10" viewBox="0 0 10 10" aria-hidden="true"><path d="M3 1l4 4-4 4" stroke="#fff" stroke-width="2" fill="none"/></svg></div>

  <!-- dating is easy -->
  <h2 class="abs heading" style="top:2802px;color:var(--white)">Dating is easy with <span>Amarelle</span></h2>
  <p class="abs body-text easy-text">Sed ut perspiciatis unde omnis iste natus error sit voluptatem accusantium remqu laudantium, totam rem aperiam, eaque ipsa quae.</p>
  <div class="abs easy-input">Email</div>
  <div class="btn btn--teal" style="left:676px;top:2940px;width:140px;height:38px">Sign up free</div>

  <!-- app -->
  <h2 class="abs app-title">Get the <span class="accent">Amarelle</span> app</h2>
  <p class="abs body-text app-text">Lorem ipsum dolor sit amet, consecte tur adipisc elit dolo. Proin ultricies vestibulum velit 3ab endum et condimentu mimetusp dolore ipsum doucibus sed dolorerem ipsu.Lorem ipsum dolor sit amet, consecte tur adipisc elit dolo. Proin ultricies vestibulum velit 3ab endum et condimentu mimetusp dolore ipsum doucibus sed dolorem ipproin ultricies vestibulum velit 3ab endum et condimentu mimetusp dolore doucibus sed dolorerem ipsu.</p>
  <div class="btn btn--coral" style="left:163px;top:3486px;width:168px;height:42px">Download now</div>
  <div class="abs" style="left:650px;top:3210px;width:400px;height:340px;background:linear-gradient(135deg,#f2f2f4,#c9c9cf);border-radius:40px;transform:rotate(-28deg) skewX(12deg)" role="img" aria-label="Smartphone showing the dating app with a couple photo"></div>

  <!-- blog -->
  <h2 class="abs heading" style="top:3720px"><span>Amarelle</span> blog</h2>
  <article class="abs card" style="left:163px">
    <div class="pic" style="background:linear-gradient(160deg,#5c3a30,#b07452)" role="img" aria-label="Blog photo of a couple"></div>
    <h4>Lorem ipsum dolor sit ame consectetur adipiscin</h4>
    <div class="meta"><span>Admin</span><span>May 17, 2018</span></div>
    <p>Sed ut perspiciatis unde omnis iste natus error sit voluptatem accusantium doloremque laudantium, totam rem aperiam, eaque ipsa quae ab illo inventore veritatis.</p>
  </article>
  <article class="abs card" style="left:463px">
    <div class="pic" style="background:linear-gradient(160deg,#c0463c,#d79a6a)" role="img" aria-label="Blog photo of a laughing couple"></div>
    <h4>Lorem ipsum dolor sit ame consectetur adipiscin</h4>
    <div class="meta"><span>Admin</span><span>May 17, 2018</span></div>
    <p>Sed ut perspiciatis unde omnis iste natus error sit voluptatem accusantium doloremque laudantium, totam rem aperiam, eaque ipsa quae ab illo inventore veritatis.</p>
  </article>
  <article class="abs card" style="left:765px">
    <div class="pic" style="background:linear-gradient(160deg,#3f5f7a,#a6826a)" role="img" aria-label="Blog photo of a couple outdoors"></div>
    <h4>Lorem ipsum dolor sit ame consectetur adipiscin</h4>
    <div class="meta"><span>Admin</span><span>May 17, 2018</span></div>
    <p>Sed ut perspiciatis unde omnis iste natus error sit voluptatem accusantium doloremque laudantium, totam rem aperiam, eaque ipsa quae ab illo inventore veritatis.</p>
  </article>

  <!-- footer -->
  <div class="abs support">
    <div class="label">SUPPORT</div>
    <div class="phone">555 014-2290</div>
    <div class="social"><i></i><i></i><i></i><i></i></div>
  </div>
  <div class="abs footer-col" style="left:487px">
    <h5>Help</h5>
    <ul><li>Dating Safety Tips</li><li>Sitemap</li><li>Help</li><li>Support</li><li>Dating</li></ul>
  </div>
  <div class="abs footer-col" style="left:697px">
    <h5>Community</h5>
    <ul><li>Chat Rooms</li><li>Dating Blog</li><li>Mobile Dating</li><li>Local Dating</li><li>International Dating</li></ul>
  </div>
  <div class="abs footer-col" style="left:935px">
    <h5>Links</h5>
    <ul><li>Privacy Policy</li><li>Terms &amp; Conditions</li><li>Affiliates</li><li>Contact Us</li><li>About Us</li></ul>
  </div>
  <div class="abs footer-rule"></div>
  <div class="abs copyright">© 2018 Amarelle. All Rights are Reserved. Privacy | Terms &amp; Conditions</div>

</div>
</body>
</html>
```